New Company Business Card design

Looking for a corporate looking business card utilising my new logo design - the logo i would like embossed as one option and flat as another - simplistic but stylish - less is more - we are an import export business launching into the market - i would like a couple of options as main background - Grey or Black

```html
<!DOCTYPE html>
<html lang="en">
<head>
<meta charset="utf-8">
<title>Meridian Trade Partners – Business Card</title>
<link rel="stylesheet" href="https://fonts.googleapis.com/css2?family=Cinzel:wght@400;600&family=Arimo:wght@400&display=swap">
<style>
  :root {
    --stage: #3a3b3d;
    --card-grey: #dedede;
    --brand-blue: #1a6fc4;
    --back-blue: #0b6fcb;
    --back-blue-light: #2a86d9;
    --ink: #2a2a2a;
    --muted: #7a7a7a;
    --rule: #b5b5b5;
    --white: #ffffff;
  }
  * { margin: 0; padding: 0; box-sizing: border-box; }
  html, body { width: 1200px; height: 896px; overflow: hidden; }
  body {
    background: var(--stage);
    font-family: "Arimo", Arial, sans-serif;
    position: relative;
  }
  .card {
    position: absolute;
    left: 280px;
    width: 640px;
    height: 366px;
    border-radius: 2px;
    overflow: hidden;
  }
  .card--front { top: 50px; background: var(--card-grey); color: var(--ink); }
  .card--back {
    top: 480px;
    background: radial-gradient(ellipse at 75% 20%, var(--back-blue-light) 0%, var(--back-blue) 60%);
    color: var(--white);
  }

  .holder { position: absolute; left: 44px; top: 48px; }
  .holder__name {
    font-family: "Cinzel", "Times New Roman", serif;
    font-size: 27px; letter-spacing: 1px;
    color: var(--brand-blue); font-weight: 400;
  }
  .holder__role { font-size: 17px; margin-top: 2px; }
  .contact { list-style: none; margin-top: 14px; }
  .contact li { display: flex; align-items: center; gap: 10px; font-size: 17px; line-height: 24px; }
  .contact svg { width: 14px; height: 14px; fill: var(--brand-blue); flex: none; }

  .brand { position: absolute; right: 40px; top: 122px; width: 300px; text-align: right; }
  .brand__mark {
    display: inline-block; width: 18px; height: 18px; border-radius: 50%;
    background: var(--brand-blue); margin-bottom: 6px;
  }
  .brand__name {
    font-family: "Cinzel", "Times New Roman", serif;
    color: var(--brand-blue); font-size: 25px; line-height: 28px; letter-spacing: 1px;
  }
  .brand__tagline {
    font-family: "Cinzel", "Times New Roman", serif;
    font-size: 10px; letter-spacing: 2px; color: var(--muted); margin-top: 6px;
    white-space: nowrap;
  }

  .divider { position: absolute; left: 44px; right: 40px; top: 252px; height: 1px; background: var(--rule); }

  .address {
    position: absolute; right: 40px; top: 274px; text-align: right;
    font-size: 18px; line-height: 24px; font-style: normal;
  }

  .back__brand { position: absolute; left: 0; right: 0; top: 110px; text-align: center; }
  .back__name {
    font-family: "Cinzel", "Times New Roman", serif;
    font-size: 32px; line-height: 36px; letter-spacing: 2px;
  }
  .back__rule { width: 420px; height: 1px; background: rgba(255,255,255,.8); margin: 10px auto 8px; }
  .back__tagline {
    font-family: "Cinzel", "Times New Roman", serif;
    font-size: 12px; letter-spacing: 4px; opacity: .9;
  }
  .back__web { position: absolute; left: 0; right: 0; top: 270px; text-align: center; font-size: 17px; letter-spacing: 1px; }
</style>
</head>
<body>
  <section class="card card--front" aria-label="Business card front">
    <div class="holder">
      <h1 class="holder__name">Daniel Hartley</h1>
      <p class="holder__role">Managing Director</p>
      <ul class="contact">
        <li><svg viewBox="0 0 16 16" aria-hidden="true"><path d="M3 1h3l1 4-2 1c1 2 3 4 5 5l1-2 4 1v3c0 1-1 2-2 2C7 15 1 9 1 3c0-1 1-2 2-2z"/></svg>044-555 210 347</li>
        <li><svg viewBox="0 0 16 16" aria-hidden="true"><path d="M4 0h8a1 1 0 0 1 1 1v14a1 1 0 0 1-1 1H4a1 1 0 0 1-1-1V1a1 1 0 0 1 1-1zm1 2v10h6V2zm3 11a1 1 0 1 0 0 2 1 1 0 0 0 0-2z"/></svg>044-555 210 348</li>
        <li><svg viewBox="0 0 16 16" aria-hidden="true"><path d="M1 3h14v10H1zm1 1v.5l6 4 6-4V4zm0 2v6h12V6l-6 4z"/></svg>hello@meridiantrade.com</li>
      </ul>
    </div>

    <div class="brand">
      <span class="brand__mark" aria-hidden="true"></span>
      <p class="brand__name">Meridian Trade<br>Partners</p>
      <p class="brand__tagline">WORLDWIDE SUPPLY FOR HOME MARKETS</p>
    </div>

    <div class="divider"></div>

    <address class="address">48 Harbour Lane<br>Portsmouth, 204518</address>
  </section>

  <section class="card card--back" aria-label="Business card back">
    <div class="back__brand">
      <p class="back__name">Meridian Trade Partners</p>
      <div class="back__rule"></div>
      <p class="back__tagline">WORLDWIDE SUPPLY FOR HOME MARKETS</p>
    </div>
    <p class="back__web">www.meridiantrade.com</p>
  </section>
</body>
</html>
```